Brellin Vale , Australian natural body care needs a new product label.

I have just had a logo designed by sketchharbor and now want this logo added to a product label design. The product is a cleansing, moisturising hand scrub with only natural ingredients and anti microbial essential oils. I have made this product for over 15 years and it needs a new more appropriate image. It was previously called morning ritual and came in a tube. the new packaging is a white pump pack container. Dimensions for the label are 185mm wide and 80mm high, I have attached a sheet with all of the information required on the label.
Updates

Target Market(s)

anyone with dry skin

Industry/Entity Type

Cosmetics

Requirements
Must have
• professional and upmarket appearance. Be creative and surprise me your take on how this label should look.
Nice to have
• Natural colours, the attached logo should be changed in colour to match the label.

```html
<!DOCTYPE html>
<html lang="en">
<head>
<meta charset="utf-8">
<title>Brellin Vale Hand Scrub – Label Colourways</title>
<link rel="stylesheet" href="https://fonts.googleapis.com/css2?family=Abril+Fatface&family=Roboto+Slab:wght@300;400;700&family=Roboto:wght@400;500&display=swap">
<style>
  :root {
    --ink: #222222;
    --paper: #ffffff;
    --frame: #111111;
    --leaf: #3f9a3c;
    --sun: #f5cb4c;
    --rose: #ee3456;
    --page: #ffffff;
  }
  * { box-sizing: border-box; margin: 0; padding: 0; }
  html, body { width: 1200px; height: 900px; overflow: hidden; background: var(--page); }
  body { position: relative; font-family: "Roboto Slab", Georgia, serif; color: var(--ink); }

  .label {
    position: absolute;
    left: 280px;
    width: 640px;
    height: 275px;
    background: var(--paper);
    border: 2px solid var(--frame);
  }
  .label--leaf { top: 26px; --accent: var(--leaf); }
  .label--sun  { top: 315px; --accent: var(--sun); }
  .label--rose { top: 604px; --accent: var(--rose); }

  .label > * { position: absolute; }

  .usage {
    left: 21px; top: 16px; width: 120px;
    font-size: 6px; line-height: 7.3px; font-weight: 300;
    color: var(--accent);
  }
  .ingredients {
    left: 21px; top: 90px; width: 118px;
    font-size: 6px; line-height: 7.3px; font-weight: 300;
  }
  .ingredients h3 { font-size: 8.5px; line-height: 9px; font-weight: 400; }
  .ingredients p { margin-top: 7px; }
  .ingredients p:first-of-type { margin-top: 0; }
  .ingredients strong { font-weight: 700; }

  .brand {
    left: 212px; top: 20px; width: 86px;
    display: flex; flex-direction: column; align-items: center; gap: 4px;
    color: var(--accent);
  }
  .brand__dot { width: 18px; height: 18px; border-radius: 50%; background: var(--accent); }
  .brand__name { font-size: 11px; font-weight: 400; letter-spacing: 0.2px; }

  .product-name {
    left: 221px; top: 108px;
    font-family: "Abril Fatface", Georgia, serif;
    font-size: 27px; line-height: 30px; letter-spacing: 0.6px;
    color: var(--accent);
  }
  .rule { left: 223px; top: 148px; width: 36px; height: 1.2px; background: var(--accent); }
  .benefits {
    left: 222px; top: 158px;
    font-size: 8px; line-height: 12.2px; font-weight: 300;
    list-style: none;
  }
  .benefits strong { font-weight: 700; }
  .origin-tag {
    left: 221px; top: 234px;
    font-size: 7.5px; font-weight: 300; color: var(--accent); letter-spacing: 0.1px;
  }
  .net-weight {
    left: 222px; top: 247px;
    font-family: "Roboto", Arial, sans-serif; font-weight: 500; font-size: 12px;
  }
  .artwork {
    left: 354px; top: 202px; width: 62px; height: 56px;
    border-radius: 40% 60% 50% 45%;
    background: radial-gradient(circle at 45% 45%, var(--accent), color-mix(in srgb, var(--accent) 75%, #ffffff));
  }

  .maker {
    left: 547px; top: 20px; width: 80px;
    font-size: 6px; line-height: 7.3px; font-weight: 400;
  }
  .maker h2 { font-size: 9px; line-height: 11px; font-weight: 400; margin-bottom: 5px; }
  .maker p + p { margin-top: 7px; }
  .handmade {
    left: 547px; top: 117px;
    font-family: "Abril Fatface", Georgia, serif;
    font-size: 8.5px; line-height: 10.5px; letter-spacing: 0.4px;
    color: var(--accent);
  }
  .symbols { left: 562px; top: 184px; display: flex; gap: 14px; align-items: flex-end; }
</style>
</head>
<body>

  <section class="label label--leaf">
    <p class="usage">All in one completely natural cleanser, exfoliate &amp; moisturiser. With refreshing &amp; uplifting antimicrobial essential oils and finely milled organic sea salt. Apply a small amount on your hands, scrub and cleanse for 60 seconds or longer. Rinse with water only and towel dry for an amazing immediate result.</p>
    <div class="ingredients">
      <h3>100% Natural ingredients;</h3>
      <p>Sunflower oil (Helianthus annuus), Sundried Sea Salt (Sodium chloride), Rosehip oil (Rosa eglanteria), Avocado oil (Persea Gratissima), Macadamia oil (Macadamia integrifolia), Jojoba oil (Simmondsia chinensis), (Wheatgerm oil (Triticum gestivum), Thixin (hydrogenated castor oil), tocopherol (Vitamin E). Essential oils of; Tea Tree (Melaleuca alternifolia), May Chang (Litsea cubeba), Lavender (Lavandular angustifolia).</p>
      <p><strong>No Alcohol, water or chemicals only pure natural products. Shake contents occasionally.</strong></p>
      <p><strong>Precaution,</strong> This product contains sun dried sea salt and stinging may</p>
    </div>
    <div class="brand"><span class="brand__dot"></span><span class="brand__name">Brellin Vale</span></div>
    <h1 class="product-name">Hand Scrub</h1>
    <span class="rule"></span>
    <ul class="benefits">
      <li>Dry &amp; damaged hand repair</li>
      <li>Immediate results</li>
      <li>Ultra-moisturising with</li>
      <li><strong>Rosehip &amp; essential oil</strong></li>
    </ul>
    <p class="origin-tag">AUSTRALIAN MADE</p>
    <p class="net-weight">250 g</p>
    <div class="artwork" role="img" aria-label="Green leaf sprig illustration"></div>
    <div class="maker">
      <h2>Brellin Vale</h2>
      <p>18 Carrow Lane<br>Halden, NSW 2290</p>
      <p>sales@brellinvale.com<br>brellinvale.com</p>
    </div>
    <p class="handmade">Hand made in<br>Sydney Australia</p>
    <div class="symbols">
      <svg width="18" height="16" viewBox="0 0 18 16" aria-label="Recyclable"><g fill="none" stroke="#111" stroke-width="2.4" stroke-linejoin="round"><path d="M9 2 L15 13 L3 13 Z"/></g><path d="M7 1 L11 1 L9 4 Z M16 11 L17 15 L13 14 Z M1 15 L2 11 L5 14 Z" fill="#111"/></svg>
      <svg width="16" height="18" viewBox="0 0 16 18" aria-label="12 months after opening"><path d="M2 8 H14 V16 Q14 17 13 17 H3 Q2 17 2 16 Z" fill="none" stroke="#111" stroke-width="0.8"/><path d="M2 6 L13 0.5" stroke="#111" stroke-width="0.9"/><text x="8" y="14" font-size="3.5" text-anchor="middle" font-family="Arial, sans-serif">12 M</text></svg>
    </div>
  </section>

  <section class="label label--sun">
    <p class="usage">All in one completely natural cleanser, exfoliate &amp; moisturiser. With refreshing &amp; uplifting antimicrobial essential oils and finely milled organic sea salt. Apply a small amount on your hands, scrub and cleanse for 60 seconds or longer. Rinse with water only and towel dry for an amazing immediate result.</p>
    <div class="ingredients">
      <h3>100% Natural ingredients;</h3>
      <p>Sunflower oil (Helianthus annuus), Sundried Sea Salt (Sodium chloride), Rosehip oil (Rosa eglanteria), Avocado oil (Persea Gratissima), Macadamia oil (Macadamia integrifolia), Jojoba oil (Simmondsia chinensis), (Wheatgerm oil (Triticum gestivum), Thixin (hydrogenated castor oil), tocopherol (Vitamin E). Essential oils of; Tea Tree (Melaleuca alternifolia), May Chang (Litsea cubeba), Lavender (Lavandular angustifolia).</p>
      <p><strong>No Alcohol, water or chemicals only pure natural products. Shake contents occasionally.</strong></p>
      <p><strong>Precaution,</strong> This product contains sun dried sea salt and stinging may</p>
    </div>
    <div class="brand"><span class="brand__dot"></span><span class="brand__name">Brellin Vale</span></div>
    <h1 class="product-name">Hand Scrub</h1>
    <span class="rule"></span>
    <ul class="benefits">
      <li>Dry &amp; damaged hand repair</li>
      <li>Immediate results</li>
      <li>Ultra-moisturising with</li>
      <li><strong>Rosehip &amp; essential oil</strong></li>
    </ul>
    <p class="origin-tag">AUSTRALIAN MADE</p>
    <p class="net-weight">250 g</p>
    <div class="artwork" role="img" aria-label="Yellow flower head illustration"></div>
    <div class="maker">
      <h2>Brellin Vale</h2>
      <p>18 Carrow Lane<br>Halden, NSW 2290</p>
      <p>sales@brellinvale.com<br>brellinvale.com</p>
    </div>
    <p class="handmade">Hand made in<br>Sydney Australia</p>
    <div class="symbols">
      <svg width="18" height="16" viewBox="0 0 18 16" aria-label="Recyclable"><g fill="none" stroke="#111" stroke-width="2.4" stroke-linejoin="round"><path d="M9 2 L15 13 L3 13 Z"/></g><path d="M7 1 L11 1 L9 4 Z M16 11 L17 15 L13 14 Z M1 15 L2 11 L5 14 Z" fill="#111"/></svg>
      <svg width="16" height="18" viewBox="0 0 16 18" aria-label="12 months after opening"><path d="M2 8 H14 V16 Q14 17 13 17 H3 Q2 17 2 16 Z" fill="none" stroke="#111" stroke-width="0.8"/><path d="M2 6 L13 0.5" stroke="#111" stroke-width="0.9"/><text x="8" y="14" font-size="3.5" text-anchor="middle" font-family="Arial, sans-serif">12 M</text></svg>
    </div>
  </section>

  <section class="label label--rose">
    <p class="usage">All in one completely natural cleanser, exfoliate &amp; moisturiser. With refreshing &amp; uplifting antimicrobial essential oils and finely milled organic sea salt. Apply a small amount on your hands, scrub and cleanse for 60 seconds or longer. Rinse with water only and towel dry for an amazing immediate result.</p>
    <div class="ingredients">
      <h3>100% Natural ingredients;</h3>
      <p>Sunflower oil (Helianthus annuus), Sundried Sea Salt (Sodium chloride), Rosehip oil (Rosa eglanteria), Avocado oil (Persea Gratissima), Macadamia oil (Macadamia integrifolia), Jojoba oil (Simmondsia chinensis), (Wheatgerm oil (Triticum gestivum), Thixin (hydrogenated castor oil), tocopherol (Vitamin E). Essential oils of; Tea Tree (Melaleuca alternifolia), May Chang (Litsea cubeba), Lavender (Lavandular angustifolia).</p>
      <p><strong>No Alcohol, water or chemicals only pure natural products. Shake contents occasionally.</strong></p>
      <p><strong>Precaution,</strong> This product contains sun dried sea salt and stinging may</p>
    </div>
    <div class="brand"><span class="brand__dot"></span><span class="brand__name">Brellin Vale</span></div>
    <h1 class="product-name">Hand Scrub</h1>
    <span class="rule"></span>
    <ul class="benefits">
      <li>Dry &amp; damaged hand repair</li>
      <li>Immediate results</li>
      <li>Ultra-moisturising with</li>
      <li><strong>Rosehip &amp; essential oil</strong></li>
    </ul>
    <p class="origin-tag">AUSTRALIAN MADE</p>
    <p class="net-weight">250 g</p>
    <div class="artwork" role="img" aria-label="Rosehip berries with leaves illustration"></div>
    <div class="maker">
      <h2>Brellin Vale</h2>
      <p>18 Carrow Lane<br>Halden, NSW 2290</p>
      <p>sales@brellinvale.com<br>brellinvale.com</p>
    </div>
    <p class="handmade">Hand made in<br>Sydney Australia</p>
    <div class="symbols">
      <svg width="18" height="16" viewBox="0 0 18 16" aria-label="Recyclable"><g fill="none" stroke="#111" stroke-width="2.4" stroke-linejoin="round"><path d="M9 2 L15 13 L3 13 Z"/></g><path d="M7 1 L11 1 L9 4 Z M16 11 L17 15 L13 14 Z M1 15 L2 11 L5 14 Z" fill="#111"/></svg>
      <svg width="16" height="18" viewBox="0 0 16 18" aria-label="12 months after opening"><path d="M2 8 H14 V16 Q14 17 13 17 H3 Q2 17 2 16 Z" fill="none" stroke="#111" stroke-width="0.8"/><path d="M2 6 L13 0.5" stroke="#111" stroke-width="0.9"/><text x="8" y="14" font-size="3.5" text-anchor="middle" font-family="Arial, sans-serif">12 M</text></svg>
    </div>
  </section>

</body>
</html>
```